Stone Over Tide - Stationery Design Project

Hi everyone,

We need a business card and a stationary set designed for a new corporate video production company based in Sydney, 'Stone Over Tide'.

The name refers to the mythological 'phoenix' so we would like to see designs that are appropriate to both the name and to a creative film company. The key thing is, we need to appear fresh and creative while maintaining professionalism.

We would like to stick with dark colors for the basis of the card. One idea that came up was obsidian/volcanic rock with the logo cracking through to reveal lava or something fire like. This is just one idea that has come up, but we are of course open to others and would love to see what people can come up with. Extensive use of flames/fire imagery is not really what we are after.

Also, cinematic as opposed to corporate is preferable.

**** UPDATE ****
When I hand over the card to a prospective client, I want them to feel like they are receiving an obsidian plate with inscriptions in it (ie the phoenix). Looking for something elemental and rigid to contrast and complement the graceful lines of the logo.

Designs we require:
- Business card
(We would like a business card that makes use of some of the more premium business card printing options, such as foil stamping, embossing/debossing, painted edges, spot UV etc. Doesnt have to use all these things, only what you feel works, but we are looking for a business card that stands out and is memorable and these nice touches have that effect. For an example of what is possible, check out "http://www.velvetprintery.net/base/category/business-card-gallery/".)

- Letter head
- With compliments slip
- Display folder

COPMPANY DETAILS:
ABN: 62 738 294 019
Company Address: 7/18-20 Kell St, Marbury NSW 2058
Name: Rex M. Dunleavy
Title: Producer
Contact Number: 0412 539 204
email: rex@stoneovertide.com
website: www.stoneovertide.com

ABOUT THE PHOENIX:
The phoenix is a musical bird from mythology, known for its long fancy tail and small plume on the top of its head. They are elegant and graceful and symbolize immortality, endurance and strength, believed to live for 5 centuries before they were reborn from their ashes.
Updates

Hi everyone,

We have just updated the design brief to include business contact information, website etc. should anyone require it for their designs.

Thanks

Rex

Target Market(s)

Other creative businesses and marketing firms.

Industry/Entity Type

Printing

Requirements
Must have
• Basic printing requirements:
- CMYK colour space
- 300dpi resolution
- Color bleed/crop marks etc to allow for trimming where necessary
- Source files upon handover
Should not have
• Overuse of fire/flame imagery

```html
<!DOCTYPE html>
<html lang="en">
<head>
<meta charset="utf-8">
<title>Stone Over Tide – Business Card</title>
<link href="https://fonts.googleapis.com/css2?family=Lato:wght@300;400;700&display=swap" rel="stylesheet">
<style>
  :root {
    --backdrop: #2e2e30;
    --card: #1c1d20;
    --card-edge: #8e1a1a;
    --ink: #e9e9ea;
    --ink-soft: #c9c9cb;
    --accent: #d2281e;
    --spot-uv: #5d5e61;
  }
  * { margin: 0; padding: 0; box-sizing: border-box; }
  html, body {
    width: 1200px; height: 900px; overflow: hidden;
    background: var(--backdrop);
    font-family: "Lato", sans-serif;
  }
  .stage {
    width: 1200px; height: 900px;
    display: flex; align-items: center; justify-content: center; gap: 48px;
  }
  .card {
    position: relative;
    width: 540px; height: 327px;
    background: var(--card);
    border-bottom: 4px solid var(--card-edge);
    box-shadow: 0 18px 40px rgba(0,0,0,.45);
  }
  /* contact side */
  .contact { padding: 36px 40px; color: var(--ink); }
  .contact__name {
    font-size: 19px; font-weight: 400; letter-spacing: .5px; text-transform: uppercase;
  }
  .contact__title { font-size: 12px; font-weight: 300; color: var(--ink-soft); margin-top: 2px; }
  .contact__list { list-style: none; margin-top: 18px; font-size: 13px; font-weight: 300; }
  .contact__list li { display: flex; align-items: center; gap: 12px; line-height: 21px; }
  .contact__list li.gap { margin-top: 12px; }
  .contact__list svg { width: 11px; height: 11px; fill: var(--accent); flex: none; }
  .contact__list .indent { padding-left: 23px; }
  .contact__web { font-weight: 700; }
  .contact__web span { color: var(--accent); }
  .wordmark {
    position: absolute; right: 40px; bottom: 44px;
    font-size: 13px; font-weight: 300; letter-spacing: 7px; color: var(--ink);
    text-transform: uppercase;
  }
  /* brand side */
  .brand { overflow: hidden; }
  .brand__uv {
    position: absolute; right: 34px; top: 120px;
    font-size: 38px; font-weight: 300; letter-spacing: 6px; text-transform: uppercase;
    color: var(--spot-uv);
  }
</style>
</head>
<body>
<main class="stage">
  <section class="card contact" aria-label="Business card, contact side">
    <h1 class="contact__name">Lena Marsh</h1>
    <p class="contact__title">Operation Manager</p>
    <ul class="contact__list">
      <li><svg viewBox="0 0 12 12"><path d="M2 1h3l1 3-2 1a7 7 0 0 0 3 3l1-2 3 1v3a1 1 0 0 1-1 1A10 10 0 0 1 1 2a1 1 0 0 1 1-1z"/></svg>+1 646 555 0142</li>
      <li><svg viewBox="0 0 12 12"><path d="M3 0h6a1 1 0 0 1 1 1v10a1 1 0 0 1-1 1H3a1 1 0 0 1-1-1V1a1 1 0 0 1 1-1zm0 2v7h6V2z"/></svg>+61 412 539 204</li>
      <li><svg viewBox="0 0 12 12"><path d="M0 2h12v8H0zm1 1v.5l5 3 5-3V3z"/></svg>name@stoneovertide.me</li>
      <li class="gap"><svg viewBox="0 0 12 12"><path d="M6 0a4 4 0 0 1 4 4c0 3-4 8-4 8S2 7 2 4a4 4 0 0 1 4-4zm0 2.5A1.5 1.5 0 1 0 6 5.5 1.5 1.5 0 0 0 6 2.5z"/></svg><span class="contact__web">www.<span>stoneovertide</span>.com</span></li>
      <li class="indent">Avenue Lucien Marot - Port Vale</li>
      <li class="indent">BP 812 - City, Country</li>
    </ul>
    <p class="wordmark">Stone Over Tide</p>
  </section>

  <section class="card brand" aria-label="Business card, brand side with spot UV name">
    <p class="brand__uv">Stone Over Tide</p>
  </section>
</main>
</body>
</html>
```